Website for virtual assistant and proofreader

Professional, feminine (but not flowery!) website offering and explaining my services as a VA and Proofreader. Probably only 7 pages: home, about, services (x2), fees, testimonials and contact page. <br/><br/>I already have most of the content, which I have uploaded so you can get an idea of waht I do. I have brand colours and logo already also uploaded. I really just need the bones of the site to be designed and am happy/capable of setting this up as a Wordpress site. I'm just rubbish at design!

Industry/Entity Type

Business Service

Coding

Coded - Design and coding required

Number of Pages Required

4 page

Other font styles liked:
• Roboto Bold + Great Vibes

Colors
3276b5
fee3d4

Requirements
Must have
• should be informative, professional, feminine. Clean, clear, CTA's links to services and fees pages
• Also, see all 3 colour codes on the attached doc.
Nice to have
• business images but place holders will do
Should not have
• Nothing flowery or cartoons! Not 'busy'

```html
<!DOCTYPE html>
<html lang="en">
<head>
<meta charset="utf-8">
<title>Clara M Hollis – Virtual Assistant and Proofreader</title>
<link href="https://fonts.googleapis.com/css2?family=Great+Vibes&family=Roboto:wght@300;400;500;700&display=swap" rel="stylesheet">
<style>
:root{
  --blue:#1d6590;
  --blue-deep:#12608a;
  --blue-soft:#3276b5;
  --peach:#f2c4b0;
  --peach-light:#fee3d4;
  --ink:#2b2b2b;
  --text:#444;
  --muted:#999;
  --footer:#f5f3f3;
  --white:#fff;
  --gold:#f2c21b;
}
*{box-sizing:border-box;margin:0;padding:0}
html,body{width:1200px;height:4381px;overflow:hidden}
body{position:relative;background:var(--white);font-family:'Roboto',sans-serif;color:var(--text)}
.abs{position:absolute}
.script{font-family:'Great Vibes',cursive;font-weight:400}
.center{text-align:center}

/* header */
.header{left:0;top:0;width:1200px;height:133px;background:var(--white);z-index:3}
.brand-disc{left:48px;top:-60px;width:150px;height:235px;border-radius:0 0 75px 75px;background:var(--white);z-index:2}
.brand{left:90px;top:68px;z-index:4;display:flex;align-items:center;gap:10px}
.brand-mark{width:34px;height:34px;border-radius:50%;background:var(--blue)}
.brand-name{font-size:22px;font-weight:500;color:var(--blue)}
.brand-sub{left:152px;top:108px;font-size:10px;font-weight:500;color:var(--blue);z-index:4}
.contact-top{top:34px;font-size:18px;display:flex;align-items:center;gap:8px;z-index:4;white-space:nowrap}
.contact-top.phone{left:640px;color:var(--blue)}
.contact-top.mail{left:860px;color:var(--muted);font-size:15px;top:36px}
.social-dot{top:41px;width:11px;height:11px;border-radius:50%;background:#aaa;z-index:4}
.nav{top:86px;right:91px;display:flex;gap:36px;font-size:15px;font-weight:500;color:var(--ink);z-index:4;white-space:nowrap}
.nav .active{color:var(--blue)}

/* hero */
.hero-photo{left:0;top:133px;width:1200px;height:598px;background:linear-gradient(115deg,#6b4b3b 0%,#c9b9aa 35%,#e8e2dc 60%,#cfc6bd 100%)}
.hero-edge{left:0;top:700px;width:1200px;height:40px}
.hero-circle{left:592px;top:189px;width:486px;height:486px;border-radius:50%;background:rgba(22,94,136,.92);color:var(--white)}
.hero-circle .script{position:absolute;left:0;width:100%;text-align:center;font-size:56px;line-height:1;white-space:nowrap}
.hero-link{position:absolute;left:0;width:100%;top:374px;text-align:center;font-size:17px;font-weight:700;text-decoration:underline}

/* about */
.about-ring{left:-130px;top:963px;width:320px;height:320px;border-radius:50%;border:62px solid var(--peach)}
.about-photo{left:94px;top:818px;width:466px;height:466px;border-radius:50%;border:5px solid var(--peach);background:linear-gradient(140deg,#b08a4d,#d9b88c 50%,#8a6a3d)}
.about-title{left:597px;top:848px;font-size:72px;color:var(--ink);white-space:nowrap}
.about-text{left:599px;top:945px;width:512px;font-size:14px;line-height:31px;color:var(--text);text-align:justify}
.btn{display:flex;align-items:center;justify-content:center;border-radius:24px;font-size:14px;font-weight:700}
.btn.blue{background:var(--blue);color:var(--white)}
.btn.peach{background:var(--peach);color:var(--ink)}

/* services */
.services{left:0;top:1378px;width:1200px;height:777px;background:linear-gradient(135deg,#a39590,#8f7f7b 50%,#a09390)}
.services-title{left:0;width:1200px;top:1450px;font-size:72px;color:var(--white)}
.services-intro{left:125px;top:1540px;width:950px;font-size:14px;line-height:29px;color:var(--white);font-weight:300}
.svc-ring{top:1656px;width:226px;height:226px;border-radius:50%;border:1.5px solid rgba(255,255,255,.85)}
.svc-ring svg{position:absolute;left:73px;top:73px}
.svc-title{top:1900px;width:240px;font-size:18px;line-height:26px;font-weight:500;color:var(--white)}
.svc-text{width:220px;font-size:14px;line-height:23px;font-weight:300;color:var(--white)}
.svc-link{width:240px;font-size:14px;font-weight:700;color:var(--white)}

/* why me */
.why-mark{left:570px;top:2280px;width:60px;height:60px;border-radius:50%;background:var(--blue)}
.why-title{left:0;width:1200px;top:2410px;font-size:78px;color:var(--ink)}
.why-text{left:255px;top:2500px;width:690px;font-size:15px;line-height:30px;color:var(--ink)}

/* certifications */
.cert{left:0;top:2675px;width:1200px;height:349px;background:var(--blue-deep)}
.cert-title{left:0;width:1200px;top:2750px;font-size:76px;color:var(--white);white-space:nowrap}
.cert-sub{left:0;width:1200px;top:2845px;font-size:16px;color:#dfe9f0}

/* testimonials */
.testi-title{left:0;width:1200px;top:3095px;font-size:72px;color:var(--ink)}
.stars{left:0;width:1200px;top:3172px;display:flex;justify-content:center;gap:8px}
.testi-text{left:150px;top:3208px;width:900px;font-size:15px;line-height:27px;color:var(--ink)}
.avatar{border-radius:50%}
.avatar.side{top:3290px;width:94px;height:94px;background:linear-gradient(150deg,#9fb8c6,#c9d7de);opacity:.8}
.avatar.main{left:543px;top:3281px;width:112px;height:112px;background:linear-gradient(150deg,#6a4a3a,#c2a38f)}
.testi-name{left:0;width:1200px;top:3408px;font-size:17px;color:var(--ink)}

/* contact */
.contact{left:0;top:3520px;width:1200px;height:620px;background:linear-gradient(135deg,#a0928e,#8e807c 55%,#a3958f)}
.contact-title{left:0;width:1200px;top:3598px;font-size:72px;color:var(--white)}
.field{background:var(--white);font-size:13px;color:#555;padding:14px 16px}
.footer-edge{left:0;top:4100px;width:1200px;height:40px}

/* footer */
.footer{left:0;top:4130px;width:1200px;height:251px;background:var(--footer)}
.f-brand{left:92px;top:4240px;display:flex;align-items:center;gap:12px}
.f-brand .brand-mark{width:48px;height:48px}
.f-brand .brand-name{font-size:32px}
.f-sub{left:176px;top:4290px;font-size:15px;font-weight:500;color:var(--blue)}
.follow{left:955px;top:4252px;font-size:11px;font-weight:700;color:var(--ink)}
.f-dot{top:4244px;width:25px;height:25px;border-radius:50%;background:var(--blue)}
.f-nav{right:88px;top:4294px;display:flex;gap:26px;font-size:15px;font-weight:500;color:var(--ink);white-space:nowrap}
.copy{right:88px;top:4333px;font-size:12px;color:var(--ink)}
</style>
</head>
<body>

<!-- header -->
<div class="abs header"></div>
<div class="abs brand-disc"></div>
<div class="abs brand"><span class="brand-mark"></span><span class="brand-name">Clara M Hollis</span></div>
<div class="abs brand-sub">Virtual Assistant and Proofreader</div>
<div class="abs contact-top phone">
  <svg width="16" height="16" viewBox="0 0 24 24" fill="none" stroke="currentColor" stroke-width="2"><path d="M5 3h4l2 5-3 2a11 11 0 0 0 6 6l2-3 5 2v4a2 2 0 0 1-2 2A17 17 0 0 1 3 5a2 2 0 0 1 2-2z"/></svg>
  +00 12 345 6789
</div>
<div class="abs contact-top mail">
  <svg width="18" height="14" viewBox="0 0 24 18" fill="none" stroke="var(--blue)" stroke-width="2"><rect x="1" y="1" width="22" height="16" rx="2"/><path d="M1 2l11 8 11-8"/></svg>
  clara@hollisva.org
</div>
<div class="abs social-dot" style="left:1066px"></div>
<div class="abs social-dot" style="left:1095px"></div>
<nav class="abs nav">
  <span class="active">Home</span><span>About</span><span>Services</span><span>Fees</span><span>Testimonials</span><span>Contact</span>
</nav>

<!-- hero -->
<div class="abs hero-photo" role="img" aria-label="Hand writing with a pen on paper at a desk"></div>
<svg class="abs hero-edge" viewBox="0 0 1200 40" preserveAspectRatio="none"><path d="M0 22 L40 16 L90 24 L150 14 L220 22 L300 12 L380 20 L460 14 L540 22 L620 12 L700 20 L780 13 L860 22 L940 14 L1020 20 L1100 12 L1200 18 V40 H0Z" fill="#fff"/></svg>
<div class="abs hero-circle">
  <div class="script" style="top:92px">Allow me...</div>
  <div class="script" style="top:152px">to handle the details</div>
  <div class="script" style="top:214px">so you can get on</div>
  <div class="script" style="top:274px">with business.</div>
  <div class="hero-link">LEARN MORE &raquo;</div>
</div>

<!-- about -->
<div class="abs about-ring"></div>
<div class="abs about-photo" role="img" aria-label="Portrait photo of the virtual assistant"></div>
<h1 class="abs about-title script">Clara M Hollis</h1>
<p class="abs about-text">Every great leader is backed by diligent and knowledgeable support. Have you ever wondered what it would be like to have your very own personal assistant? Well, you can. A virtual assistant can do everything a full-time assistant can, with the added bonus that she can save you money. Whether you need daily help, or help with special assignments or big projects, hiring me as your VA will save you the costs typically associated with an employee–holiday pay,sick pay, overtime, taxes, and insurance, are no longer your concern.</p>
<div class="abs btn blue" style="left:599px;top:1190px;width:163px;height:46px">LEARN MORE</div>

<!-- services -->
<div class="abs services" role="img" aria-label="Woman working on a laptop in a home office, softened behind a taupe overlay"></div>
<h2 class="abs services-title script center">Services</h2>
<p class="abs services-intro center">Do you need some Smart Office Support (SOS)? Do you have a huge project looming on the horizon? Do you just need a little support managing the growing stacks of To-Dos cluttering your desk? As a master of managing the barrage of daily details that require concise and prompt attention, SOS is my speciality, from organisation to proofreading, no detail is too small!</p>

<div class="abs svc-ring" style="left:96px"><svg width="80" height="80" viewBox="0 0 80 80" fill="none" stroke="#fff" stroke-width="2"><rect x="10" y="10" width="44" height="56" rx="3"/><path d="M18 24h28M18 34h20M18 44h16"/><circle cx="58" cy="56" r="10"/></svg></div>
<div class="abs svc-ring" style="left:356px"><svg width="80" height="80" viewBox="0 0 80 80" fill="none" stroke="#fff" stroke-width="2"><rect x="8" y="14" width="64" height="42" rx="3"/><path d="M30 66h20M40 56v10M50 44v-14M58 44v-20M42 44v-8"/></svg></div>
<div class="abs svc-ring" style="left:617px"><svg width="80" height="80" viewBox="0 0 80 80" fill="none" stroke="#fff" stroke-width="2"><rect x="14" y="8" width="56" height="48" rx="3"/><path d="M14 18h56M42 28l10 4v8c0 6-10 10-10 10s-10-4-10-10v-8z"/><circle cx="20" cy="58" r="7"/><path d="M8 74c0-8 24-8 24 0"/></svg></div>
<div class="abs svc-ring" style="left:877px"><svg width="80" height="80" viewBox="0 0 80 80" fill="none" stroke="#fff" stroke-width="2"><rect x="8" y="12" width="44" height="56" rx="3"/><path d="M16 26h20M16 36h14M16 46h18"/><circle cx="50" cy="46" r="12"/><path d="M59 55l12 12"/></svg></div>

<div class="abs svc-title center" style="left:90px">Organizational Service &amp;<br>Project Management</div>
<div class="abs svc-title center" style="left:350px">Administrative and<br>Accounting Support</div>
<div class="abs svc-title center" style="left:610px">Website Administration</div>
<div class="abs svc-title center" style="left:872px">Editorial Services and<br>Proofreading</div>

<div class="abs svc-text center" style="left:100px;top:1965px">Reliable project and team management, master of organisation</div>
<div class="abs svc-text center" style="left:360px;top:1965px">Work smarter not harder with the right VA by your side</div>
<div class="abs svc-text center" style="left:620px;top:1943px">Dependable and reliable website updates–like clockwork</div>
<div class="abs svc-text center" style="left:882px;top:1965px">Catching simple typos and grammatical faux pas to preserve your integrity</div>

<div class="abs svc-link center" style="left:90px;top:2050px">LEARN MORE &raquo;</div>
<div class="abs svc-link center" style="left:350px;top:2028px">LEARN MORE &raquo;</div>
<div class="abs svc-link center" style="left:610px;top:2007px">LEARN MORE &raquo;</div>
<div class="abs svc-link center" style="left:872px;top:2050px">LEARN MORE &raquo;</div>

<!-- why me -->
<div class="abs why-mark"></div>
<h2 class="abs why-title script center">Why Me?</h2>
<p class="abs why-text center">I offer administrative, management, and editorial services for those in need of an expert, professional, and discreet "virtual" assistant. As an independent contractor, I can offer you these services with all the same dedication and loyalty as a full-time staff assistant -- at a more cost-effective rate</p>

<!-- certifications -->
<div class="abs cert"></div>
<h2 class="abs cert-title script center">Certifications And Qualifications</h2>
<p class="abs cert-sub center">Professional Certificate for Proofreading</p>
<div class="abs btn peach" style="left:520px;top:2889px;width:162px;height:45px">LEARN MORE</div>

<!-- testimonials -->
<h2 class="abs testi-title script center">Testimonials</h2>
<div class="abs stars">
  <svg width="16" height="16" viewBox="0 0 24 24"><path d="M12 2l3 7 7 .6-5.4 4.7 1.7 7.2L12 17.6 5.7 21.5l1.7-7.2L2 9.6 9 9z" fill="var(--gold)"/></svg>
  <svg width="16" height="16" viewBox="0 0 24 24"><path d="M12 2l3 7 7 .6-5.4 4.7 1.7 7.2L12 17.6 5.7 21.5l1.7-7.2L2 9.6 9 9z" fill="var(--gold)"/></svg>
  <svg width="16" height="16" viewBox="0 0 24 24"><path d="M12 2l3 7 7 .6-5.4 4.7 1.7 7.2L12 17.6 5.7 21.5l1.7-7.2L2 9.6 9 9z" fill="var(--gold)"/></svg>
  <svg width="16" height="16" viewBox="0 0 24 24"><path d="M12 2l3 7 7 .6-5.4 4.7 1.7 7.2L12 17.6 5.7 21.5l1.7-7.2L2 9.6 9 9z" fill="var(--gold)"/></svg>
  <svg width="16" height="16" viewBox="0 0 24 24"><path d="M12 2l3 7 7 .6-5.4 4.7 1.7 7.2L12 17.6 5.7 21.5l1.7-7.2L2 9.6 9 9z" fill="var(--gold)"/></svg>
</div>
<p class="abs testi-text center">Lorem ipsum dolor sit amet, consectetur adipiscing elit, sed do eiusmod tempor incididunt ut labore et dolore magna aliqua.<br>Ut enim ad minim veniam, quis nostrud exerco laboris nisnsequat.</p>
<div class="abs avatar side" style="left:400px" role="img" aria-label="Client photo"></div>
<div class="abs avatar main" role="img" aria-label="Client photo"></div>
<div class="abs avatar side" style="left:703px" role="img" aria-label="Client photo"></div>
<p class="abs testi-name center">Megan R., Seaview, US</p>

<!-- contact -->
<div class="abs contact" role="img" aria-label="Woman working at a desk, softened behind a taupe overlay"></div>
<h2 class="abs contact-title script center">Contact Us</h2>
<div class="abs field" style="left:369px;top:3686px;width:223px;height:44px">Name</div>
<div class="abs field" style="left:609px;top:3686px;width:223px;height:44px">Email</div>
<div class="abs field" style="left:369px;top:3748px;width:223px;height:43px">Phone</div>
<div class="abs field" style="left:609px;top:3748px;width:223px;height:43px">Title</div>
<div class="abs field" style="left:369px;top:3811px;width:463px;height:150px">Message</div>
<div class="abs btn blue" style="left:520px;top:3983px;width:162px;height:44px">SUBMIT</div>
<svg class="abs footer-edge" viewBox="0 0 1200 40" preserveAspectRatio="none"><path d="M0 18 L60 12 L130 22 L210 12 L290 20 L370 11 L450 20 L530 13 L610 22 L690 12 L770 20 L850 12 L930 21 L1010 13 L1090 20 L1200 14 V40 H0Z" fill="var(--footer)"/></svg>

<!-- footer -->
<div class="abs footer"></div>
<div class="abs f-brand"><span class="brand-mark"></span><span class="brand-name">Clara M Hollis</span></div>
<div class="abs f-sub">Virtual Assistant and Proofreader</div>
<div class="abs follow">FOLLOW</div>
<div class="abs f-dot" style="left:1022px"></div>
<div class="abs f-dot" style="left:1054px"></div>
<div class="abs f-dot" style="left:1086px"></div>
<nav class="abs f-nav"><span>HOME</span><span>SERVICES</span><span>SYSTEM APPLICATIONS</span><span>FEES WHY ME?</span><span>CONTACT</span></nav>
<p class="abs copy">Copyright © 2020 All Rights Reserved</p>

</body>
</html>
```